Mesh Banner Design for Business Premises

We require the design of a large mesh banner to be installed across the front fence of our warehouse. The banner should prominently feature our existing Rigmore logo and brand colours (yellow, white, and black) and be designed to be highly visible from the road.

The overall aesthetic should be strong, masculine, and industrial, reflecting the nature of the scaffolding and construction industry. The background should be predominantly black, with our branding incorporated in yellow and white for strong contrast and readability.

The banner should clearly communicate the full scope of services we provide, including:

Scaffold Design
Scaffold Engineering
Scaffold Installation / Erection
Scaffold Dismantling

It should also indicate the types of projects and clients we service, including:

Commercial
Industrial
Residential
Civil

The design should feel bold and professional, with a construction-oriented style that aligns with the scaffolding industry. It should be clean, impactful, and easy to read from a distance, ensuring passing traffic can quickly understand our services.

Where possible, subtle industrial or structural design elements (such as scaffold components, steel textures, or linework) may be incorporated into the background to reinforce the industry theme while keeping the layout uncluttered.

The final design will be produced as a large-format mesh banner for outdoor installation, so it should be created with this application and viewing distance in mind.

```html
<!DOCTYPE html>
<html lang="en">
<head>
<meta charset="utf-8">
<title>Rigmore Mesh Banner</title>
<link href="https://fonts.googleapis.com/css2?family=Oswald:wght@500;600&display=swap" rel="stylesheet">
<style>
  :root {
    --page: #e6e6e6;
    --charcoal: #333333;
    --ink: #363230;
    --yellow: #fbb424;
    --yellow-deep: #f6a11c;
    --yellow-light: #fcc13a;
    --white: #ffffff;
  }
  * { margin: 0; padding: 0; box-sizing: border-box; }
  html, body {
    width: 1200px; height: 1001px; overflow: hidden;
    background: var(--page);
    font-family: "Oswald", "Arial Narrow", sans-serif;
  }
  .banner {
    position: absolute; left: 48px; top: 402px;
    width: 1094px; height: 196px;
    display: flex;
    box-shadow: 40px 26px 34px -18px rgba(0,0,0,0.45);
  }
  .brand-panel {
    position: relative;
    width: 302px; height: 100%;
    background: var(--charcoal);
    display: flex; flex-direction: column; align-items: center; justify-content: center;
  }
  .brand-name {
    display: flex; align-items: center; gap: 12px;
    color: var(--white);
    font-weight: 500; font-size: 26px; letter-spacing: 9px;
    margin-top: -6px;
  }
  .brand-mark { width: 16px; height: 16px; background: var(--yellow); }
  .brand-phone {
    color: var(--yellow);
    font-weight: 500; font-size: 38px; line-height: 1;
    margin-top: 8px; letter-spacing: 0.5px;
  }
  .hazard-left { position: absolute; left: 50px; bottom: 0; }
  .services-panel {
    position: relative; flex: 1; height: 100%;
    overflow: hidden;
  }
  .site-photo {
    position: absolute; inset: 0;
    background: linear-gradient(115deg, var(--yellow-deep) 0%, var(--yellow) 45%, var(--yellow-light) 70%, var(--yellow) 100%);
  }
  .hazard-right { position: absolute; right: 58px; top: 0; }
  .list {
    position: absolute; top: 30px;
    list-style: none;
    color: var(--ink);
    font-weight: 600; font-size: 29px; line-height: 37px;
    letter-spacing: 0.6px;
  }
  .list-sectors { left: 32px; }
  .list-services { left: 443px; }
</style>
</head>
<body>
  <section class="banner">
    <div class="brand-panel">
      <div class="brand-name"><span class="brand-mark"></span>RIGMORE</div>
      <div class="brand-phone">1300 7 BUILD</div>
      <svg class="hazard-left" width="72" height="16" viewBox="0 0 72 16" aria-hidden="true">
        <polygon points="8,0 20,0 12,16 0,16" fill="#fff"/>
        <polygon points="32,0 44,0 36,16 24,16" fill="#fff"/>
        <polygon points="56,0 68,0 60,16 48,16" fill="#fff"/>
      </svg>
    </div>
    <div class="services-panel">
      <div class="site-photo" role="img" aria-label="Scaffolders working on a steel scaffold frame, tinted yellow"></div>
      <svg class="hazard-right" width="72" height="16" viewBox="0 0 72 16" aria-hidden="true">
        <polygon points="8,0 20,0 12,16 0,16" fill="#fff"/>
        <polygon points="32,0 44,0 36,16 24,16" fill="#fff"/>
        <polygon points="56,0 68,0 60,16 48,16" fill="#fff"/>
      </svg>
      <ul class="list list-sectors">
        <li>COMMERCIAL</li>
        <li>INDUSTRIAL</li>
        <li>RESIDENTIAL</li>
        <li>CIVIL</li>
      </ul>
      <ul class="list list-services">
        <li>SCAFFOLD DESIGN</li>
        <li>SCAFFOLD ENGINEERING</li>
        <li>SCAFFOLD INSTALLATION</li>
        <li>SCAFFOLD DISMANTLING</li>
      </ul>
    </div>
  </section>
</body>
</html>
```